HR services to some of biggest Silicon Valley Tech companies needs a new website

We need a new website design probably 4-5 pages initially. Here are some websites we like the look of https://quillmarkgroup.example/ , https://www.vantrel.example/ and https://pemvio.example/ .

Target Market(s)

Silicon valley tech companies

Industry/Entity Type

HR

Coding

Coded - Design and coding required

Number of Pages Required

5+ page

Requirements
Nice to have
• any stock photos or images should show a diverse group of people. Our client base is very diverse

```html
<!DOCTYPE html>
<html lang="en">
<head>
<meta charset="utf-8">
<title>Kestrel Peak HR</title>
<link href="https://fonts.googleapis.com/css2?family=Jost:wght@400;500;600;700&display=swap" rel="stylesheet">
<style>
:root{
  --yellow:#fdc300;
  --charcoal:#565658;
  --ink:#2f2f31;
  --body:#555;
  --paper:#ffffff;
  --mist:#f3f3f3;
  --line:#e3e3e3;
}
*{box-sizing:border-box;margin:0;padding:0}
html,body{width:1200px;height:4773px;overflow:hidden}
body{font-family:'Jost',sans-serif;color:var(--ink);background:var(--paper);position:relative}
.abs{position:absolute}
.photo{position:absolute}
.brand{display:flex;align-items:center;gap:12px;color:var(--paper);font-weight:600;font-size:26px;letter-spacing:1px;white-space:nowrap}
.brand-dot{width:34px;height:34px;border-radius:50%;background:var(--yellow);flex:none}
.topbar{position:absolute;left:0;top:0;width:1200px;height:104px;background:var(--charcoal)}
.topbar .brand{position:absolute;left:89px;top:32px}
.nav{position:absolute;left:449px;top:44px;display:flex;gap:46px;font-size:13px;font-weight:600;color:var(--paper);letter-spacing:.5px}
.nav .active{color:var(--yellow)}
.btn{display:inline-block;font-weight:600;font-size:12px;letter-spacing:.6px;text-transform:uppercase;padding:0 22px;line-height:40px;background:var(--yellow);color:var(--ink);white-space:nowrap}
.btn-dark{background:var(--charcoal);color:var(--yellow)}
.btn-light{background:var(--paper);color:var(--ink)}
.nav-cta{position:absolute;left:968px;top:30px;line-height:42px;padding:0 20px}
.hero-title{position:absolute;left:209px;top:272px;color:var(--paper);font-size:52px;font-weight:600;line-height:1.1}
.hero-sub{position:absolute;left:209px;top:336px;color:var(--paper);font-size:36px;font-weight:500}
.hero-cta{position:absolute;left:209px;top:412px}
.h2{font-size:38px;font-weight:500;line-height:1.1;color:var(--ink)}
.h2 em{font-style:normal;color:var(--yellow)}
.points{list-style:none}
.points li{position:relative;padding-left:56px;font-size:13px;line-height:19px;color:var(--body);margin-bottom:20px}
.points li::before{content:"";position:absolute;left:0;top:2px;width:22px;height:22px;border-radius:50%;border:3px solid var(--yellow)}
.frame{position:absolute;background:var(--yellow)}
.shot{position:absolute;border-radius:0 0 60px 0}
.svc-title{font-size:22px;font-weight:500;color:var(--paper);margin:18px 0 8px}
.svc-list{list-style:none}
.svc-list li{position:relative;padding-left:26px;font-size:13px;line-height:19px;color:var(--paper);margin-bottom:10px}
.svc-list li::before{content:"";position:absolute;left:0;top:3px;width:11px;height:11px;border-radius:50%;border:1.5px solid currentColor}
.svc{position:absolute}
.svc-featured{background:var(--yellow);padding:38px 32px}
.svc-featured .svc-title,.svc-featured .svc-list li{color:#6b5a14}
.field{background:var(--paper);height:36px;font-size:12px;color:#666;padding:9px 14px}
.foot-h{font-size:16px;font-weight:600;color:var(--ink);letter-spacing:.6px;margin-bottom:18px}
.foot-t{font-size:12px;color:var(--body);line-height:24px}
</style>
</head>
<body>

<header class="topbar">
  <div class="brand"><span class="brand-dot"></span>KESTREL PEAK HR</div>
  <nav class="nav"><span class="active">HOME</span><span>ABOUT US</span><span>SERVICES</span><span>TEAM</span><span>CONTACT US</span></nav>
  <span class="btn nav-cta">Consult now!</span>
</header>

<section class="hero">
  <div class="photo" role="img" aria-label="Diverse team working together around laptops in an office" style="left:0;top:104px;width:1200px;height:630px;background:linear-gradient(120deg,#3e5778,#7b90aa 55%,#b7c3cf)"></div>
  <svg class="abs" style="left:0;top:540px" width="1200" height="206" viewBox="0 0 1200 206">
    <polygon points="0,35 598,192 1200,20 1200,206 0,206" fill="var(--yellow)"/>
    <polygon points="0,20 598,170 1200,0 1200,206 0,206" fill="var(--paper)"/>
  </svg>
  <h1 class="hero-title">KESTREL PEAK HR</h1>
  <p class="hero-sub">Our Team Supports Yours</p>
  <span class="btn hero-cta">Explore more</span>
</section>

<section class="about">
  <div class="frame" style="left:89px;top:995px;width:183px;height:265px"></div>
  <div class="shot photo" role="img" aria-label="Group of cheerful colleagues celebrating" style="left:111px;top:781px;width:376px;height:456px;background:linear-gradient(160deg,#9bb3cf,#d8dde3)"></div>
  <h2 class="h2 abs" style="left:617px;top:822px">Celebrating <em>15 years</em> in<br>business</h2>
  <ul class="points abs" style="left:617px;top:922px;width:490px">
    <li>For fifteen years our team of industry experts has been providing HR consulting services with innovative strategies and a partnership mentality</li>
    <li>We have worked with some of the most innovative companies in Silicon Valley, across a broad range of industries, and we're proud to grow our client list every year</li>
    <li>Kestrel Peak's experienced professionals help implement and maintain best practices, allowing our clients to focus on their core competencies</li>
  </ul>
  <span class="btn abs" style="left:617px;top:1168px">Contact us</span>
</section>

<section class="services">
  <svg class="abs" style="left:0;top:1290px" width="1200" height="1240" viewBox="0 0 1200 1240">
    <polygon points="0,127 860,0 1200,127 1200,1100 335,1238 0,1100" fill="var(--yellow)"/>
    <polygon points="0,140 860,16 1200,140 1200,1092 335,1220 0,1092" fill="var(--charcoal)"/>
  </svg>
  <h2 class="abs" style="left:0;top:1410px;width:1200px;text-align:center;color:var(--paper);font-size:38px;font-weight:500">Our services</h2>
  <p class="abs" style="left:0;top:1458px;width:1200px;text-align:center;color:var(--paper);font-size:18px;line-height:23px">We help assess your HR needs and offer ongoing HR Department services or defined<br>projects based on your organization's unique needs and goals</p>

  <div class="abs" style="left:88px;top:1959px;width:490px;height:1px;background:#6d6d70"></div>
  <div class="abs" style="left:600px;top:1975px;width:1px;height:350px;background:#6d6d70"></div>

  <div class="svc" style="left:120px;top:1583px;width:440px">
    <svg width="80" height="80" viewBox="0 0 80 80" fill="none" stroke="var(--yellow)" stroke-width="4"><circle cx="40" cy="40" r="28" stroke-dasharray="10 6"/><circle cx="40" cy="40" r="19"/><circle cx="40" cy="35" r="6"/><path d="M29 51c3-7 19-7 22 0"/></svg>
    <h3 class="svc-title">Setup</h3>
    <ul class="svc-list">
      <li>Manage leave administration between client, employee and vendor(s)</li>
      <li>Create Company Handbook</li>
      <li>Write termination procedure</li>
      <li>Set up benefits services</li>
      <li>Set up workers comp vendor</li>
      <li>Create job descriptions for current and anticipated roles</li>
    </ul>
  </div>

  <div class="svc svc-featured" style="left:600px;top:1545px;width:511px;height:414px">
    <svg width="82" height="82" viewBox="0 0 82 82" fill="none" stroke="#6b5a14" stroke-width="4"><circle cx="18" cy="14" r="8"/><circle cx="64" cy="14" r="8"/><path d="M4 36c2-9 26-9 28 0M50 36c2-9 26-9 28 0"/><circle cx="38" cy="52" r="14"/><path d="M28 62L12 78"/></svg>
    <h3 class="svc-title">Managing HR functions/recruiting</h3>
    <ul class="svc-list">
      <li>Onboarding/Offboarding</li><li>Employee relations</li><li>Investigations</li><li>Leave administration</li><li>Immigration liaison</li><li>Compensation management</li><li>Full cycle recruitment</li>
    </ul>
  </div>

  <div class="svc" style="left:120px;top:2014px;width:440px">
    <svg width="80" height="80" viewBox="0 0 80 80" fill="none" stroke="var(--yellow)" stroke-width="4"><rect x="4" y="4" width="72" height="72" rx="8"/><path d="M4 20h72"/><path d="M28 46a13 13 0 1 0 4-10M26 32v8h8"/></svg>
    <h3 class="svc-title">Recurring procedures</h3>
    <ul class="svc-list">
      <li>Review handbook annually</li><li>Roll out training (required and soft skills training)</li><li>Write offer letters</li><li>Handle employee data and files</li><li>Conduct I-9 audits</li><li>Handle merit and review bonuses</li>
    </ul>
  </div>

  <div class="svc" style="left:632px;top:2014px;width:440px">
    <svg width="82" height="80" viewBox="0 0 82 80" fill="none" stroke="var(--yellow)" stroke-width="4"><path d="M4 6h52v34H26l-12 10V40H4z"/><path d="M14 18h32M14 28h22"/><path d="M62 30h16v32h-8v10l-12-10H34V48"/><path d="M46 58l6 6 12-12"/></svg>
    <h3 class="svc-title">Partner communications &amp; projects</h3>
    <ul class="svc-list">
      <li>Manage annual bidding process for benefits review</li><li>Handle workers compensation claims administration</li><li>Manage leave administration between client, employee and vendor(s)</li><li>Handle EDD inquires</li><li>Partner on M&amp;A activity</li>
    </ul>
  </div>
</section>

<section class="solution">
  <h2 class="h2 abs" style="left:88px;top:2642px">Your <em>human resources</em><br>solution</h2>
  <ul class="points abs" style="left:88px;top:2742px;width:500px">
    <li>Kestrel Peak HR is the solution to all your HR issues. We are a one-stop-shop providing a variety of services</li>
    <li>Whether you have a specific HR need or seek relief by outsourcing altogether, we have you covered</li>
    <li>For some clients, a Kestrel Peak Consultant is known as the HR department and for others, we simply step in as needed on a project basis</li>
  </ul>
  <span class="btn btn-dark abs" style="left:88px;top:2945px">Consult now!</span>
  <div class="frame" style="left:928px;top:2805px;width:183px;height:262px"></div>
  <div class="photo" role="img" aria-label="Business partners shaking hands in a meeting" style="left:713px;top:2589px;width:374px;height:448px;border-radius:0 0 0 60px;background:linear-gradient(160deg,#cdd3da,#6e7b8c)"></div>
</section>

<section class="team">
  <div class="frame" style="left:89px;top:3362px;width:183px;height:262px"></div>
  <div class="shot photo" role="img" aria-label="Diverse group of professionals standing together" style="left:111px;top:3148px;width:376px;height:454px;background:linear-gradient(160deg,#e9ecef,#7d8590)"></div>
  <h2 class="h2 abs" style="left:617px;top:3210px">Our <em>team</em></h2>
  <ul class="points abs" style="left:617px;top:3270px;width:490px">
    <li>Our team is woman-owned, women-led and partnership-oriented</li>
    <li>Working with us means you're hiring senior-level talent that acts as an extension of your company</li>
    <li>We're here to educate companies and help them solve complex HR problems</li>
    <li>Information about our CEO, Maren Holt, can be found here</li>
  </ul>
  <span class="btn abs" style="left:617px;top:3496px">Contact us</span>
</section>

<section class="cta">
  <svg class="abs" style="left:0;top:3648px" width="1200" height="222" viewBox="0 0 1200 222">
    <polygon points="0,40 598,0 1200,40 1200,222 0,222" fill="var(--yellow)"/>
    <polygon points="0,52 598,14 1200,52 1200,222 0,222" fill="var(--charcoal)"/>
  </svg>
  <span class="abs" style="left:582px;top:3704px;width:36px;height:36px;border-radius:50%;background:var(--yellow)"></span>
  <h2 class="abs" style="left:88px;top:3776px;color:var(--paper);font-size:38px;font-weight:500">We look forward to working with you</h2>
  <span class="btn btn-light abs" style="left:865px;top:3782px;line-height:38px;width:246px;padding:0;text-align:center;font-size:11px;letter-spacing:.4px">Start work with Kestrel Peak</span>
</section>

<section class="contact">
  <div class="abs" style="left:991px;top:3867px;width:209px;height:519px;background:var(--charcoal)"></div>
  <div class="photo" role="img" aria-label="Two women using phones at a cafe table" style="left:0;top:3867px;width:991px;height:519px;background:linear-gradient(120deg,#6a5446,#b59a84 50%,#e6ddd3)"></div>
  <div class="abs" style="left:600px;top:3930px;width:600px;height:393px;background:var(--yellow);border-radius:120px 0 0 0">
    <h3 style="position:absolute;left:0;top:30px;width:100%;text-align:center;font-size:28px;font-weight:500;line-height:30px;color:var(--charcoal)">Contact us for a free<br>consultation</h3>
    <div class="field abs" style="left:72px;top:106px;width:212px">Your Name</div>
    <div class="field abs" style="left:298px;top:106px;width:213px">Email</div>
    <div class="field abs" style="left:72px;top:162px;width:212px">Phone</div>
    <div class="field abs" style="left:298px;top:162px;width:213px">Services</div>
    <div class="field abs" style="left:72px;top:218px;width:439px;height:80px">Description ...</div>
    <span class="btn btn-dark abs" style="left:232px;top:314px;width:128px;padding:0;text-align:center;line-height:38px">Submit</span>
  </div>
</section>

<footer>
  <div class="abs" style="left:0;top:4386px;width:1200px;height:387px;background:var(--mist)"></div>
  <div class="brand abs" style="left:88px;top:4542px;color:var(--charcoal);font-size:20px;gap:10px"><span class="brand-dot" style="width:28px;height:28px"></span>KESTREL PEAK HR</div>
  <div class="abs" style="left:352px;top:4478px">
    <div class="foot-h">CONTACT US</div>
    <div class="foot-t" style="padding-left:24px;position:relative;line-height:20px"><svg style="position:absolute;left:0;top:2px" width="14" height="18" viewBox="0 0 14 18" fill="none" stroke="#555" stroke-width="1.5"><path d="M7 17s6-6 6-10A6 6 0 0 0 1 7c0 4 6 10 6 10z"/><circle cx="7" cy="7" r="2"/></svg>48 Harbor View Rd, Suite # 210<br>Easton, MA, 02356</div>
    <div class="foot-t" style="padding-left:24px;position:relative;margin-top:10px"><svg style="position:absolute;left:0;top:5px" width="14" height="14" viewBox="0 0 14 14" fill="none" stroke="#555" stroke-width="1.5"><path d="M2 1h3l1.5 3.5-2 1.5a8 8 0 0 0 3.5 3.5l1.5-2L13 9v3a1 1 0 0 1-1 1A11 11 0 0 1 1 2a1 1 0 0 1 1-1z"/></svg>+ 555-014-2290</div>
    <div class="foot-t" style="padding-left:24px;position:relative;margin-top:6px"><svg style="position:absolute;left:0;top:7px" width="14" height="11" viewBox="0 0 14 11" fill="none" stroke="#555" stroke-width="1.5"><rect x="1" y="1" width="12" height="9"/><path d="M1 1l6 5 6-5"/></svg>info@kestrelpeakhr.example</div>
  </div>
  <div class="abs" style="left:672px;top:4478px">
    <div class="foot-h">QUICK LINKS</div>
    <div class="foot-t">Home<br>About Us<br>Services<br>Team<br>Contact Us</div>
  </div>
  <div class="abs" style="left:880px;top:4478px">
    <div class="foot-h">FOLLOW US</div>
    <div style="display:flex;gap:10px" aria-label="Social media links">
      <span style="width:28px;height:28px;border-radius:50%;background:var(--charcoal)"></span>
      <span style="width:28px;height:28px;border-radius:50%;background:var(--yellow)"></span>
      <span style="width:28px;height:28px;border-radius:50%;background:var(--charcoal)"></span>
      <span style="width:28px;height:28px;border-radius:50%;background:var(--charcoal)"></span>
    </div>
  </div>
  <div class="abs foot-t" style="left:88px;top:4724px;font-size:11px">© 2021 <b>Kestrel Peak HR</b>. All Right Reserved</div>
</footer>

</body>
</html>
```